Brochure, website and corporate stationary Design Project

Project scope:
1 x brochure (A4 insert) design
1 x brochure folder design (both external pages and one internal (there will be a few lines of text on the left inside page). The internal right side page will be a pocket for brochures (A4 inserts)
1 x corporate stationary pack (Business Card, logo (a proper logo file format needs to be produced), Letterhead and Envelope)
1 x concept design for our website. You dont need to do the coding. What you need to deliver is the design in a standard format (i.e. photoshop or blend)
Summary: the scope of the project is to design our brochure and its brochure folder, corporate stationary design and graphics concept design for our website. You should also consider our existing logo when performing the above design work (you can modify the logo slightly if you think it would improve look and feel and relevancy to overall design).
• We are a small IT services company
• The folder will be used to hold the brochures (inserts). The folder will be given to prospect customers (see attached a sample service brochure called “VelmaroX User support services Ver0.1.docx”)
• On the cover of the folder, we want to have a design that uses keywords / phrases that reflects our main services (see attached file called “Phrases for presentation folder.docs”). Please note that not all phrases have to be used, use a logic in which ones or add new suggestions
• Inside the folder, at left side we want to have a short text explaining about our services a bit (see attached file called “Brochure Main section v0.91.docx”)
• All designs (corporate stationary, brochure, folder, web, etc.) must be consistent with each other and follow same concept, colour scheme, etc
• you are allowed to do minor changes to our existing logo if you have good reason to do so (see attached logo)
• We want our website design to be simple, elegant, not very colourful, light. HTML5. No flash. (you dont need to do the actual coding of the website, just deliver the design in Photoshop, Blend or any other standard format) With minimal menu items such as: home, services, about us, news, contact us, and other important ones if any. Same colour and design scheme as corporate stationary and brochures
• The company name “VelmaroX” is derived from the Swedish word “Grön” (meaning green) and “roX” which stands for technology but spelled with a “Q” to resemble Quality. The corporate green colour comes from the word “Grön”.
• All templates must be delivered in a standard editable format
Reason: To provide more time to the designers to come with their design submissions.
please note that we more than doubled the budget for this project
Target Market(s)
We deliver IT services to companies of 3-4 employees upto 200-300 employees. The brochures are intended for prospect customers (non IT people)
Industry/Entity Type
Business
Look and feel

```html
<!DOCTYPE html>
<html lang="en">
<head>
<meta charset="utf-8">
<title>VelmaroX – User support services folder</title>
<link href="https://fonts.googleapis.com/css2?family=Fira+Sans:wght@400;500;600&display=swap" rel="stylesheet">
<style>
:root{
  --stage:#30353a;
  --paper:#ffffff;
  --green:#8dc63f;
  --panel:#6c7071;
  --panel-text:#f1f2f2;
  --light:#f2f2f2;
  --cloud:#d8d9d9;
  --ink:#4a4d4f;
  --ink-soft:#333536;
}
*{box-sizing:border-box;margin:0;padding:0}
html,body{width:1200px;height:1126px;overflow:hidden;background:var(--stage);font-family:"Fira Sans",Arial,sans-serif}
.spread{position:absolute;left:0;top:139px;width:1200px;height:848px;background:var(--paper);overflow:hidden}
.head{position:absolute;left:0;top:0;width:1200px;height:240px;background:var(--paper)}
.brand{position:absolute;top:100px}
.brand-name{font-size:30px;font-weight:500;color:var(--ink);letter-spacing:1.5px;line-height:1}
.brand-url{font-size:8px;font-weight:600;color:var(--ink-soft);margin-top:8px}
.brand.back{left:28px}
.brand.front{left:649px}
.contact{position:absolute;left:377px;top:64px;font-size:8px;line-height:11px;color:var(--ink-soft);font-style:normal}
.contact b{font-weight:600}
.contact p{margin-bottom:11px}
.contact dl{display:grid;grid-template-columns:36px auto}
.contact dt{font-weight:600}
.hero-image{position:absolute;left:935px;top:0;width:265px;height:240px;
  background:radial-gradient(circle at 62% 58%,#9ed04f 0,#7cb732 22%,#cfd2d3 40%,#8d9193 62%,#f4f4f4 88%)}
.rule{position:absolute;left:0;top:240px;width:1200px;height:5px;background:var(--green)}
.inside{position:absolute;left:0;top:245px;width:599px;height:575px;background:var(--panel);color:var(--panel-text)}
.inside h1{position:absolute;left:28px;top:22px;width:120px;font-size:18px;font-weight:500;line-height:21px;color:#fff}
.col{position:absolute;top:24px;font-size:7.2px;line-height:11px}
.col.one{left:159px;width:200px}
.col.two{left:377px;width:205px}
.col p{margin-bottom:11px}
.col h2{font-size:7.2px;font-weight:600;color:var(--green);margin-top:6px}
.col h2.gap{margin-top:12px}
.col strong{font-weight:600;color:#fff}
.col ul{list-style:none}
.col li::before{content:"\25CF  ";font-size:6px}
.foot{position:absolute;left:0;top:820px;width:599px;height:28px;background:var(--green)}
.foot-box{position:absolute;left:40px;top:0;width:69px;height:28px;background:var(--paper)}
.cloud{position:absolute;left:599px;top:245px;width:601px;height:603px;background:var(--light);overflow:hidden}
.row{position:absolute;white-space:nowrap;font-size:14px;line-height:16px;color:var(--green)}
.row .pre{position:absolute;right:100%;padding-right:6px;color:var(--cloud)}
.row .post{padding-left:6px;color:var(--cloud)}
</style>
</head>
<body>
<div class="spread">
  <header class="head">
    <div class="brand back"><div class="brand-name">VELMAROX</div><div class="brand-url">www.velmarox.com</div></div>
    <address class="contact">
      <p><b>VELMAROX</b><br>Building 7, 3rd Floor<br>Harbour Tech Park, Dubai , U.A.E.</p>
      <p><b>Mail Address:</b><br>PO BOX: 418 360<br>Harbour Tech Park, U.A.E.</p>
      <dl><dt>Phone:</dt><dd>+971 50 555 0142</dd><dt>Fax:</dt><dd>+971 4 555 0187</dd></dl>
    </address>
    <div class="brand front"><div class="brand-name">VELMAROX</div><div class="brand-url">www.velmarox.com</div></div>
    <div class="hero-image" role="img" aria-label="Green target ball with darts among grey target balls"></div>
  </header>
  <div class="rule"></div>

  <section class="inside">
    <h1>User support services</h1>
    <div class="col one">
      <p>With VelmaroX IT Solutions, you get a single dedicated partner for software, hardware, and user support. We provide our support packages, with a focus on practice efficiency and minimised downtime. With our Pay-As-You-Go and flat fee User Support packages, you receive remote and onsite IT support covering monitoring, maintenance, backup data protection, and experienced tech support.</p>
      <p>Sign up for any of our User Support Services and your users will be a phone call or email away from receiving the high quality desktop support they need. By using the latest support software tools, we can offer remote support as well as on-premises support through all of all support packages. The remote support makes it possible for us to assist you even when you are on business trips away from the office.</p>
      <p>Combine our User Desktop Support with our Network &amp;Server support packages for maximizing support quality and value for money</p>
      <h2>BRONZE</h2>
      <strong>Per month:</strong> AED 1200 + 300 / user<br>
      <strong>Description:</strong> The bronze package is a Pay-As-You-Go service. It is suitable for business environments that would require on-demand reactive user support.<br>
      <strong>Summary:</strong>
      <ul>
        <li>We will install remote sw on users' PCs</li>
        <li>Support requests through email and phone</li>
        <li>Support delivered work days and work hours. Physical visit to your office included whenever a remote support is not sufficient</li>
        <li>Support is delivered on a Pay-As-You-Go basis; AED 300 / hour.</li>
      </ul>
      <h2 class="gap">SILVER</h2>
      <strong>Per month:</strong> AED 2000 + 1500 / user<br>
      <strong>Description:</strong> The Silver package is a flat fee service. It also includes in-depth preventive maintenance of your users PCs or Laptops. It is suitable for business environments that would require high quality proactive user support yet want to avoid a variable monthly user support cost.
    </div>
    <div class="col two">
      <strong>Summary:</strong>
      <ul>
        <li>We will install remote sw on PCs</li>
        <li>Support requests through email and phone</li>
        <li>Support delivered work days and work hours. Physical visit to your office included whenever a remote support is not sufficient</li>
        <li>Periodic remote maintenance on PCs (service pack, health check etc.)</li>
        <li>Notebook support</li>
        <li>All support hours spent included at no additional cost.</li>
      </ul>
      <h2 class="gap">GOLD</h2>
      <strong>Per month:</strong> AED 2000 + 1700 / user<br>
      <strong>Description:</strong> The Gold package is a flat fee service. As with Silver package, it includes in depth preventive maintenance of your users PCs or Laptops. However it also includes comprehensive hosted Quorvex Mailserver email services, Quorvex Teamdesk services, and Quorvex Deskline Suite licenses for all included users (all mentioned applications always latest versions). It is suitable for business environments that would require total care, A to Z high quality proactive user support yet want to avoid a variable monthly user support and IT software and services cost.<br>
      <strong>Summary:</strong>
      <ul>
        <li>We will install remote sw on PCs</li>
        <li>Support requests through email and phone</li>
        <li>Support delivered work days and work hours. Physical visit to your office included whenever a remote support is not sufficient</li>
        <li>Periodic remote maintenance on PCs (service pack, health check etc.)</li>
        <li>Notebook support</li>
        <li>Quorvex mailserver mailboxes + Quorvex Teamdesk + Quorvex Deskline Suite for all included users</li>
        <li>All support hours spent included at no additional cost.</li>
      </ul>
      <h2 class="gap">TAILOR-MADE USER SUPPORT</h2>
      We would tailor make our User Support, if your business would require so. We would attend meetings with you to hear you and understand your concerns, analyse your requirement and recommend the right level of support for ultimate alignment with your business objectives.
    </div>
  </section>
  <div class="foot"><div class="foot-box"></div></div>

  <section class="cloud" aria-label="Service keywords">
    <div class="row" style="left:200px;top:131px"><span class="pre">HOSTING CLOUD EMAIL POSTLINE</span>IT SERVICE LEVEL AGREEMENT<span class="post">IT HELPDESK SERVICES IT SECURITY</span></div>
    <div class="row" style="left:213px;top:155px"><span class="pre">EMAIL POSTLINE WEB DEVELOPMENT</span>IT HELPDESK SERVICES<span class="post">IT INFRASTRUCTURE NETWORK CLOUD</span></div>
    <div class="row" style="left:252px;top:179px"><span class="pre">DEPLOYMENT BUSINESS PROCESS MANAGEMENT</span>IT SECURITY<span class="post">CONSULTANCY BUSINESS APPLICATIONS ERP</span></div>
    <div class="row" style="left:227px;top:203px"><span class="pre">IT HELPDESK SERVICES IT SECURITY</span>IT INFRASTRUCTURE<span class="post">CLOUD SERVICES HOSTED EMAIL HOSTED</span></div>
    <div class="row" style="left:263px;top:227px"><span class="pre">SS CONSULTANCY BUSINESS APPLICATIONS</span>NETWORK<span class="post">ACCOUNTING SOFTWARE SEO SEARCH ENGINE</span></div>
    <div class="row" style="left:236px;top:252px"><span class="pre">CURITY IT INFRASTRUCTURE NETWORK</span>CLOUD SERVICES<span class="post">POSTLINE QUORVEX WEB DEVELOPMENT</span></div>
    <div class="row" style="left:245px;top:276px"><span class="pre">APPLICATIONS ERP CRM ACCOUNTING</span>HOSTED EMAIL<span class="post">SEO SEARCH ENGINE OPTIMIZATION IT</span></div>
    <div class="row" style="left:219px;top:300px"><span class="pre">SEO SEARCH ENGINE OPTIMIZATION</span>APPLICATION HOSTING<span class="post">IT SERVICE LEVEL AGREEMENT IT HELP</span></div>
    <div class="row" style="left:225px;top:324px"><span class="pre">NIL HOSTED MAILSERVER APPLICATION</span>HOSTED MAILSERVER<span class="post">EMAIL POSTLINE QUORVEX BUSINESS PR</span></div>
    <div class="row" style="left:252px;top:348px"><span class="pre">NAGE APPLICATION HOSTING CLOUD EMAIL</span>CLOUD EMAIL<span class="post">DEVELOPMENT BUSINESS PROCESS MANAGE</span></div>
    <div class="row" style="left:264px;top:373px"><span class="pre">IT SUPPORT IT SERVICE LEVEL AGREEMENT</span>POSTLINE<span class="post">SERVICES IT SECURITY IT INFRASTRUCTURE</span></div>
    <div class="row" style="left:254px;top:397px"><span class="pre">WEB DEVELOPMENT BUSINESS PROCESS</span>QUORVEX<span class="post">IT MANAGEMENT CONSULTANCY BUSINESS A</span></div>
    <div class="row" style="left:235px;top:421px"><span class="pre">SEO SEARCH ENGINE OPTIMIZATION</span>WEB DEVELOPMENT<span class="post">IT SERVICE LEVEL AGREEMENT IT HELPD</span></div>
    <div class="row" style="left:189px;top:445px"><span class="pre">HOSTING CLOUD EMAIL POSTLINE</span>BUSINESS PROCESS MANAGEMENT<span class="post">IT HELPDESK SERVICES IT SECUR</span></div>
    <div class="row" style="left:197px;top:469px"><span class="pre">POSTLINE WEB DEVELOPMENT</span>IT MANAGEMENT CONSULTANCY<span class="post">IT INFRASTRUCTURE NETWORK CLO</span></div>
    <div class="row" style="left:211px;top:494px"><span class="pre">BUSINESS PROCESS MANAGEMENT</span>BUSINESS APPLICATIONS<span class="post">CONSULTANCY BUSINESS APPLICATION</span></div>
    <div class="row" style="left:281px;top:518px"><span class="pre">PROCESS CONSULTANCY BUSINESS APPLICATIONS</span>ERP<span class="post">ACCOUNTING SOFTWARE SEO SEARCH ENGINE IT</span></div>
    <div class="row" style="left:279px;top:542px"><span class="pre">AGREEMENT IT HELPDESK SERVICES IT SECURITY</span>CRM<span class="post">CLOUD SERVICES HOSTED EMAIL HOSTED PROCE</span></div>
  </section>
</div>
</body>
</html>
```